Family business needs stationery redesign with new logo

Family owned company, established in 1987 wanting a brand 'refresh'. We are an electrical, refrigeration and construction company based in the Barkly Region Northern Territory, Australia. We have a new logo we would like to use which is uploaded along with our current letterhead and email signature. We are also dropping the word 'contractors' so please do not include this on any designs. Please note also, the 'orange' color used in our logo and designs should be Northern Territory red ochre which is as follows:

RGB (Hex): #C75B12
PantoneĀ® 159 C
CMYK: 1 / 74 / 100 / 7

We are needing our stationery redesigned using our new logo. Please include letterheads, business cards, envelopes, and email signatures.

We currently use our business letterheads for quotations, invoices, letters, HR matters, and internal memos.

We also need a separate simplified letterhead for internal paperwork such as employee leave forms, meeting agendas, and meeting minutes etc.
Updates

Reason: Needing more submissions of full package designs. We are wanting all our stationery, including business cards, letterheads, email signatures, envelopes, etc to be cohesive. We also require ALL the information, as supplied on our template letterhead, to be included on the new letterhead designs. including electrical license no.etc Thank you, K&M

Reason: needing more time as work has got in the way of looking over designs. A lot of designs not meeting the brief/criteria.

Industry/Entity Type

Business

Colors
0355a3
f37122

Requirements
Must have
• The 'orange' color used in the designs should be Northern Territory red ochre which is as follows:
• RGB (Hex): #C75B12
• PantoneĀ® 159 C
• CMYK: 1 / 74 / 100 / 7
• ***MUST INCLUDE ALL INFORMATION THAT IS ON OUR CURRENT LETTERHEAD***
Should not have
• Please do not include the word 'contractors'

```html
<!DOCTYPE html>
<html lang="en">
<head>
<meta charset="utf-8">
<title>K&amp;M Letterhead</title>
<link href="https://fonts.googleapis.com/css2?family=Roboto+Condensed:wght@400;700&display=swap" rel="stylesheet">
<style>
  :root {
    --ochre: #c75b12;
    --navy: #1f2f78;
    --line-blue: #34449a;
    --paper: #ffffff;
    --backdrop: #f0d7d2;
    --text: #3a3a3a;
    --watermark: #e8e9f3;
  }
  * { margin: 0; padding: 0; box-sizing: border-box; }
  html, body { width: 1200px; height: 784px; overflow: hidden; }
  body {
    background: var(--backdrop);
    font-family: "Roboto Condensed", Arial, sans-serif;
    position: relative;
  }
  .letterhead {
    position: absolute;
    left: 338px; top: 22px;
    width: 523px; height: 740px;
    background: var(--paper);
    box-shadow: 0 2px 8px rgba(120, 70, 60, 0.18);
  }
  .edge-line { position: absolute; height: 4px; }
  .edge-line--ochre { background: var(--ochre); }
  .edge-line--blue { background: var(--line-blue); }

  .header-rule-left { top: 0; left: 0; width: 150px; }
  .header-rule-right { top: 0; left: 300px; right: 0; }

  .brand {
    position: absolute;
    top: 10px; left: 150px; width: 150px;
    text-align: center;
  }
  .brand-name {
    display: flex; align-items: center; justify-content: center; gap: 6px;
    font-weight: 700; font-size: 34px; line-height: 1;
    color: var(--navy);
  }
  .brand-dot {
    width: 12px; height: 12px; border-radius: 50%;
    background: var(--ochre);
  }
  .brand-services {
    margin-top: 5px;
    font-size: 7.5px; color: var(--text); letter-spacing: 0.1px;
    white-space: nowrap;
  }
  .brand-services .sep { color: var(--ochre); padding: 0 2px; }

  .watermark {
    position: absolute;
    top: 250px; left: 0; right: 0;
    text-align: center;
    font-weight: 700; font-size: 150px; line-height: 1;
    color: var(--watermark);
  }

  .footer-contacts {
    position: absolute;
    left: 0; right: 0; bottom: 16px;
    height: 30px;
  }
  .contact {
    position: absolute; bottom: 0;
    font-size: 7px; color: var(--text); white-space: nowrap;
  }
  .contact-icon {
    display: block;
    width: 9px; height: 9px; margin: 0 0 6px 14px;
  }
  .footer-rule-left { bottom: 0; left: 0; width: 75%; }
  .footer-rule-right { bottom: 0; left: 77%; right: 0; }
</style>
</head>
<body>
  <main class="letterhead">
    <div class="edge-line edge-line--ochre header-rule-left"></div>
    <div class="edge-line edge-line--blue header-rule-right"></div>

    <header class="brand">
      <div class="brand-name"><span class="brand-dot"></span>K&amp;M</div>
      <p class="brand-services">Electrical<span class="sep">|</span>Refrigeration<span class="sep">|</span>Building Services</p>
    </header>

    <div class="watermark" aria-hidden="true">K&amp;M</div>

    <footer class="footer-contacts">
      <div class="contact" style="left:14px">
        <svg class="contact-icon" viewBox="0 0 10 10"><circle cx="5" cy="5" r="5" fill="#1f2f78"/><path d="M5 2.2a1.9 1.9 0 0 1 1.9 1.9C6.9 5.5 5 7.8 5 7.8S3.1 5.5 3.1 4.1A1.9 1.9 0 0 1 5 2.2z" fill="#fff"/></svg>
        PO Box 2240 | 52 Warrego Rd, Barkly NT 0862
      </div>
      <div class="contact" style="left:178px">
        <svg class="contact-icon" viewBox="0 0 10 10"><circle cx="5" cy="5" r="5" fill="#1f2f78"/><path d="M3 2.5l1.2 0 .5 1.4-.7.6a4 4 0 0 0 1.5 1.5l.6-.7 1.4.5v1.2c-2.6.2-4.7-1.9-4.5-4.5z" fill="#fff"/></svg>
        08 8900 1234
      </div>
      <div class="contact" style="left:236px">
        <svg class="contact-icon" viewBox="0 0 10 10"><circle cx="5" cy="5" r="5" fill="#1f2f78"/><rect x="3.5" y="2" width="3" height="6" rx="0.6" fill="#fff"/></svg>
        0412 345 678
      </div>
      <div class="contact" style="left:294px">
        <svg class="contact-icon" viewBox="0 0 10 10"><circle cx="5" cy="5" r="5" fill="#1f2f78"/><rect x="2.5" y="4" width="5" height="3.2" fill="#fff"/><rect x="3.4" y="2.4" width="3.2" height="1.4" fill="#fff"/></svg>
        08 8900 1299
      </div>
      <div class="contact" style="left:352px">
        <svg class="contact-icon" viewBox="0 0 10 10"><circle cx="5" cy="5" r="5" fill="#1f2f78"/><rect x="2.4" y="3.2" width="5.2" height="3.6" fill="#fff"/><path d="M2.4 3.2 5 5.3l2.6-2.1" fill="none" stroke="#1f2f78" stroke-width="0.6"/></svg>
        contact@kmservices.com.au
      </div>
      <div class="contact" style="left:440px">
        <svg class="contact-icon" viewBox="0 0 10 10"><circle cx="5" cy="5" r="5" fill="#1f2f78"/><circle cx="5" cy="5" r="2.6" fill="none" stroke="#fff" stroke-width="0.7"/><path d="M2.4 5h5.2M5 2.4c-1.4 1.6-1.4 3.6 0 5.2M5 2.4c1.4 1.6 1.4 3.6 0 5.2" fill="none" stroke="#fff" stroke-width="0.5"/></svg>
        www.kmservices.com.au
      </div>
    </footer>

    <div class="edge-line edge-line--ochre footer-rule-left"></div>
    <div class="edge-line edge-line--blue footer-rule-right"></div>
  </main>
</body>
</html>
```